Postcard Design Project

Education- charter school- elementary k-6th grades- performing arts integrated in to the core curriculum

Industry/Entity Type

School

```html
<!DOCTYPE html>
<html lang="en">
<head>
<meta charset="utf-8">
<title>Bright Stage Community School – Enrollment Postcard</title>
<link rel="stylesheet" href="https://fonts.googleapis.com/css2?family=Great+Vibes&family=Montserrat:wght@400;700&family=Oswald:wght@400;500&family=Roboto+Condensed:ital,wght@0,300;0,400;1,300&family=Ubuntu:wght@500;700&display=swap">
<style>
  :root {
    --canvas-bg: #ecebe8;
    --white: #ffffff;
    --navy: #2b3a8f;
    --indigo: #2f3596;
    --magenta: #e83e8c;
    --pink-band: #ea3f8f;
    --purple: #7b4fa3;
    --yellow: #f7e600;
    --ink: #1b1b1b;
    --teal-text: #2d5a73;
    --line: #8a8a8a;
  }
  * { box-sizing: border-box; margin: 0; padding: 0; }
  html, body { width: 1200px; height: 1200px; overflow: hidden; }
  body { background: var(--canvas-bg); position: relative; font-family: "Montserrat", sans-serif; }

  .card { position: absolute; background: var(--white); box-shadow: 0 2px 8px rgba(0,0,0,.18); overflow: hidden; }

  .brand-name { font-family: "Roboto Condensed", sans-serif; font-weight: 300; color: var(--teal-text); display: inline-flex; align-items: center; gap: 6px; white-space: nowrap; }
  .brand-dot { border-radius: 50%; background: var(--purple); display: inline-block; }

  /* ---------- Front ---------- */
  .front { left: 46px; top: 242px; width: 440px; height: 645px; }
  .front .brand { position: absolute; left: 0; top: 110px; width: 260px; text-align: center; }
  .front .brand-name { font-size: 15px; }
  .front .brand-dot { width: 14px; height: 14px; }

  .front .hero-art { position: absolute; inset: 0; }
  .dancer-photo { position: absolute; left: 150px; top: 160px; width: 250px; height: 220px; background: radial-gradient(ellipse at 50% 50%, #b9a79a 0%, #c9cbcf 60%, rgba(207,210,214,0) 80%); }

  .enroll { position: absolute; left: 22px; top: 178px; transform: rotate(-5deg); transform-origin: left top; color: var(--navy); }
  .enroll-title { font-family: "Ubuntu", sans-serif; font-weight: 700; font-size: 29px; line-height: 27px; }
  .enroll-sub { font-family: "Ubuntu", sans-serif; font-weight: 500; font-size: 18px; line-height: 20px; margin-top: 6px; margin-left: 4px; color: var(--indigo); }

  .burst { position: absolute; left: 28px; top: 272px; width: 120px; height: 120px; }
  .burst-text { position: absolute; left: 58px; top: 310px; transform: rotate(-15deg); text-align: center; font-family: "Oswald", sans-serif; color: var(--ink); line-height: 1; width: 64px; }
  .burst-text .big { font-size: 20px; font-weight: 500; }
  .burst-text .small { font-size: 10px; }

  .snapshot { position: absolute; background: var(--white); padding: 5px; box-shadow: 0 2px 5px rgba(0,0,0,.3); }
  .snapshot .photo { width: 100%; height: 100%; }
  .snap-singers { left: 246px; top: 312px; width: 152px; height: 108px; transform: rotate(4deg); }
  .snap-singers .photo { background: linear-gradient(160deg, #d9d4d0, #c8403a 70%, #b32e2a); }
  .snap-guitar { left: 236px; top: 410px; width: 182px; height: 124px; transform: rotate(-4deg); }
  .snap-guitar .photo { background: linear-gradient(180deg, #9fc07a, #6f9a4e 45%, #c98a4e 75%, #e6c6b6); }

  .intro { position: absolute; left: 22px; top: 410px; width: 200px; font-family: "Roboto Condensed", sans-serif; font-style: italic; font-weight: 300; font-size: 13px; line-height: 14px; color: var(--white); }
  .intro-name { position: absolute; left: 22px; top: 490px; font-family: "Ubuntu", sans-serif; font-weight: 700; font-size: 15px; line-height: 17px; color: var(--indigo); text-shadow: 0 0 2px #fff, 0 0 2px #fff; }

  .slogan-band { position: absolute; left: 0; top: 538px; width: 440px; height: 38px; background: var(--indigo); border-top: 2px solid #fff; border-bottom: 2px solid #fff; color: var(--white); font-family: "Great Vibes", cursive; font-size: 28px; text-align: center; line-height: 34px; white-space: nowrap; }
  .contact-band { position: absolute; left: 0; top: 576px; width: 440px; height: 69px; background: var(--pink-band); display: grid; grid-template-columns: 1fr 1fr 1fr; color: var(--white); text-align: center; }
  .contact-label { font-family: "Ubuntu", sans-serif; font-weight: 500; font-size: 21px; margin-top: 4px; }
  .contact-value { font-family: "Oswald", sans-serif; font-size: 10px; line-height: 11px; margin-top: 4px; }
  .contact-value.phone { font-size: 20px; line-height: 22px; margin-top: 2px; }

  /* ---------- Back ---------- */
  .back { left: 507px; top: 345px; width: 645px; height: 438px; }
  .message-panel { position: absolute; left: 15px; top: 15px; width: 294px; height: 408px;
    background:
      radial-gradient(ellipse at 85% 15%, rgba(120,200,240,.9), rgba(120,200,240,0) 45%),
      radial-gradient(ellipse at 30% 60%, rgba(230,150,180,.9), rgba(230,150,180,0) 50%),
      radial-gradient(ellipse at 80% 80%, rgba(150,80,180,.8), rgba(150,80,180,0) 50%),
      linear-gradient(160deg, #6c74c8 0%, #8fb6e6 30%, #c99ac0 60%, #a04ab0 100%); }
  .message { position: absolute; left: 17px; top: 28px; width: 250px; color: var(--ink); font-size: 11px; line-height: 13px; }
  .message h2 { font-size: 17px; line-height: 17px; font-weight: 700; margin-bottom: 6px; }
  .message p { margin-bottom: 6px; }
  .message .cta { font-weight: 700; }
  .return-address { position: absolute; left: 17px; top: 339px; font-size: 9px; line-height: 12px; font-weight: 700; font-style: normal; text-transform: uppercase; color: var(--ink); }

  .back .brand { position: absolute; left: 322px; top: 108px; width: 190px; text-align: center; }
  .back .brand-name { font-size: 11px; }
  .back .brand-dot { width: 10px; height: 10px; }
  .stamp-box { position: absolute; left: 525px; top: 53px; width: 83px; height: 83px; border: 2px solid #222; }
  .address-line { position: absolute; left: 329px; width: 277px; height: 1px; background: var(--line); }
</style>
</head>
<body>

<section class="card front" aria-label="Postcard front">
  <div class="brand">
    <div class="brand-name"><span class="brand-dot"></span>Bright Stage Community School</div>
  </div>

  <svg class="hero-art" width="440" height="645" viewBox="0 0 440 645" aria-hidden="true">
    <defs>
      <linearGradient id="lowerGrad" x1="0" y1="0" x2="0" y2="1">
        <stop offset="0" stop-color="#6f79c2"/>
        <stop offset="0.55" stop-color="#b14aa8"/>
        <stop offset="1" stop-color="#e0449a"/>
      </linearGradient>
      <linearGradient id="greyGrad" x1="0" y1="0" x2="1" y2="0">
        <stop offset="0" stop-color="#d3d5d8"/>
        <stop offset="1" stop-color="#c4c7cb"/>
      </linearGradient>
    </defs>
    <polygon points="0,170 440,135 440,365 0,402" fill="url(#greyGrad)"/>
    <polygon points="0,402 440,365 440,540 0,540" fill="url(#lowerGrad)"/>
    <polygon points="0,170 440,135 440,141 0,176" fill="var(--magenta)"/>
    <polygon points="0,176 440,141 440,146 0,181" fill="#fff"/>
    <polygon points="0,396 440,359 440,365 0,402" fill="#fff"/>
    <polygon points="0,402 440,365 440,370 0,407" fill="var(--magenta)"/>
  </svg>

  <div class="dancer-photo" role="img" aria-label="Photo of a young dancer in a leaping pose"></div>

  <div class="enroll">
    <div class="enroll-title">Now<br>Enrolling</div>
    <div class="enroll-sub">2016-17 for<br>Grades k-6th</div>
  </div>

  <svg class="burst" viewBox="0 0 120 120" aria-hidden="true">
    <polygon fill="var(--yellow)" points="60,2 68,38 92,10 82,44 118,34 88,58 118,80 82,74 94,112 66,84 56,118 50,82 22,108 34,74 2,80 30,58 4,30 38,42 30,8 52,36"/>
  </svg>
  <div class="burst-text"><div class="big">JOIN</div><div class="small">THE ACADEMY<br>TODAY!</div></div>

  <div class="snapshot snap-singers"><div class="photo" role="img" aria-label="Photo of children singing together"></div></div>
  <div class="snapshot snap-guitar"><div class="photo" role="img" aria-label="Photo of two young children playing a guitar outdoors"></div></div>

  <p class="intro">Bright Stage Community School is the most innovative public elementary school program in Central Ohio through integration of the fine arts in all subjects.</p>
  <div class="intro-name">Bright Stage<br>Community School</div>

  <div class="slogan-band">Where Young Talent Takes The Stage</div>
  <div class="contact-band">
    <div><div class="contact-label">Venue</div><div class="contact-value">250 MAPLE GROVE ROAD<br>SPRINGFIELD, OHIO 45500</div></div>
    <div><div class="contact-label">Call</div><div class="contact-value phone">(555) 014-2270</div></div>
    <div><div class="contact-label">Web</div><div class="contact-value">WWW.BRIGHTSTAGESCHOOL.COM</div></div>
  </div>
</section>

<section class="card back" aria-label="Postcard back">
  <div class="message-panel">
    <div class="message">
      <h2>All grade levels take visual arts, music, drama, and dance.</h2>
      <p>Small class sizes with Highly Qualified teachers in the core subjects, beautiful facilities with a five acre campus provide for an outdoor learning experience, and a dedicated staff committed to a positive learning environment are just a few reasons that</p>
      <p>you will be amazed by this performing arts community school.</p>
      <p>Breakfast and lunch are provided at no cost to you! All of this tuition free! Please contact us for a tour of our school.</p>
      <p class="cta">Classes fill up quickly so call today to ensure your child's enrollment for the 2016-17 school year.</p>
    </div>
    <address class="return-address">
      Bright Stage Community School<br>
      250 Maple Grove Road<br>
      Springfield, Ohio 45500<br>
      Phone (555) 014-2270
    </address>
  </div>

  <div class="brand">
    <div class="brand-name"><span class="brand-dot"></span>Bright Stage Community School</div>
  </div>
  <div class="stamp-box" aria-label="Stamp area"></div>
  <div class="address-line" style="top:218px"></div>
  <div class="address-line" style="top:273px"></div>
  <div class="address-line" style="top:329px"></div>
  <div class="address-line" style="top:383px"></div>
</section>

</body>
</html>
```